Stationery Design Project

KT7 Staffing requires letterhead and business card designs for a company based in London. Just like the name, we're a management resourcing company, providing resources to third party companies. You can see www.kt7staffing-example.com for ideas on existing colour schemes and design concepts that have been implimented and agreed to. Ultimately the design should broadcast professionalism, safety and the concept of growth.

Target Market(s)

Financial institutes; friendly societies (All UK based)

Industry/Entity Type

Safety

Requirements
Must have
• Files produced should be print ready; and the text in them editable (eg address, name etc)

```html
<!DOCTYPE html>
<html lang="en">
<head>
<meta charset="utf-8">
<title>KT7 Staffing – Stationery</title>
<link rel="stylesheet" href="https://fonts.googleapis.com/css2?family=Arimo:wght@400;700&display=swap">
<style>
  :root {
    --backdrop: #1c8987;
    --paper: #ffffff;
    --ink-teal: #1a8a8c;
    --ink-blue: #5ab4d0;
    --rule: #8fcbdc;
    --edge: #222222;
  }
  * { margin: 0; padding: 0; box-sizing: border-box; }
  html, body { width: 1200px; height: 900px; overflow: hidden; }
  body {
    background: var(--backdrop);
    font-family: "Arimo", Arial, sans-serif;
    color: var(--ink-teal);
    position: relative;
  }

  .brand { display: flex; align-items: center; gap: 6px; }
  .brand-mark { background: var(--ink-blue); flex: none; }
  .brand-name { color: var(--ink-teal); font-weight: 700; white-space: nowrap; letter-spacing: -0.2px; }

  /* Letterhead */
  .letterhead {
    position: absolute; left: 475px; top: 25px;
    width: 595px; height: 840px;
    background: var(--paper);
    border: 1px solid var(--edge);
    z-index: 1;
  }
  .letterhead .brand { position: absolute; left: 40px; top: 34px; }
  .letterhead .brand-mark { width: 26px; height: 26px; }
  .letterhead .brand-name { font-size: 24px; }
  .letterhead-footer {
    position: absolute; left: 71px; top: 782px;
    border-left: 1px solid var(--rule);
    padding-left: 6px;
    font-size: 7px; line-height: 9.5px;
  }

  /* Business cards */
  .business-card {
    position: absolute;
    width: 241px; height: 155px;
    background: var(--paper);
    border: 1px solid var(--edge);
  }
  .business-card--back   { left: 134px; top: 341px; z-index: 2; }
  .business-card--front  { left: 288px; top: 265px; z-index: 3; }
  .business-card--lower  { left: 330px; top: 520px; z-index: 3; }

  .business-card .brand { position: absolute; left: 17px; top: 18px; }
  .business-card .brand-mark { width: 16px; height: 16px; }
  .business-card .brand-name { font-size: 15px; }
  .card-details {
    position: absolute; left: 43px; top: 70px;
    border-left: 1px solid var(--rule);
    padding-left: 3px;
  }
  .person-name { font-size: 8.5px; font-weight: 700; line-height: 11px; }
  .person-role { font-size: 7.5px; line-height: 10px; margin-bottom: 14px; }
  .contact-lines { font-size: 5.4px; line-height: 7px; white-space: nowrap; }
</style>
</head>
<body>

  <section class="letterhead" aria-label="Letterhead">
    <div class="brand">
      <span class="brand-mark"></span>
      <span class="brand-name">KT7 Staffing</span>
    </div>
    <footer class="letterhead-footer">
      <p>1st Line of address 1st Line of address 1st Line of address 1st Line of address 1st Line of address</p>
      <p>Tel: 00000 000000&nbsp; Fax: 00000 000000&nbsp; Mobile: 00000 000 000</p>
      <p>Website: www.kt7staffing-example.com&nbsp; Email: a.n.other@oooooooo</p>
    </footer>
  </section>

  <section class="business-card business-card--back" aria-label="Business card">
    <div class="brand">
      <span class="brand-mark"></span>
      <span class="brand-name">KT7 Staffing</span>
    </div>
    <div class="card-details">
      <p class="person-name">A.N. Other</p>
      <p class="person-role">Operations Manager</p>
      <div class="contact-lines">
        <p>1st Line of address 1st Line of address</p>
        <p>2nd Line of address 2nd Line of address</p>
        <p>3rd Line of address 2nd Line of address</p>
        <p>Tel: 00000 000000&nbsp; Fax: 00000 000000&nbsp; Mobile: 00000 000 000</p>
        <p>Website: www.kt7staffing-example.com&nbsp; Email: a.n.other@oooooooo</p>
      </div>
    </div>
  </section>

  <section class="business-card business-card--front" aria-label="Business card">
    <div class="brand">
      <span class="brand-mark"></span>
      <span class="brand-name">KT7 Staffing</span>
    </div>
    <div class="card-details">
      <p class="person-name">A.N. Other</p>
      <p class="person-role">Operations Manager</p>
      <div class="contact-lines">
        <p>1st Line of address 1st Line of address</p>
        <p>2nd Line of address 2nd Line of address</p>
        <p>3rd Line of address 2nd Line of address</p>
        <p>Tel: 00000 000000&nbsp; Fax: 00000 000000&nbsp; Mobile: 00000 000 000</p>
        <p>Website: www.kt7staffing-example.com&nbsp; Email: a.n.other@oooooooo</p>
      </div>
    </div>
  </section>

  <section class="business-card business-card--lower" aria-label="Business card">
    <div class="brand">
      <span class="brand-mark"></span>
      <span class="brand-name">KT7 Staffing</span>
    </div>
    <div class="card-details">
      <p class="person-name">A.N. Other</p>
      <p class="person-role">Operations Manager</p>
      <div class="contact-lines">
        <p>1st Line of address 1st Line of address</p>
        <p>2nd Line of address 2nd Line of address</p>
        <p>3rd Line of address 2nd Line of address</p>
        <p>Tel: 00000 000000&nbsp; Fax: 00000 000000&nbsp; Mobile: 00000 000 000</p>
        <p>Website: www.kt7staffing-example.com&nbsp; Email: a.n.other@oooooooo</p>
      </div>
    </div>
  </section>

</body>
</html>
```